Business cards for financial advisor-insurance agent firm

Our company, Harlow Pemberton Insurance & Investments, is an insurance (health, life, home, auto, etc) and investment brokerage offering a suite of options to meet client needs. We need business cards that are professional and embody strength, security and sophistication.

Also running a letterhead project at
http://jobs.briefmarlo.com/job.aspx?id=519087

Target Market(s)

Upper middle class and wealthy

Industry/Entity Type

Investment

Requirements
Nice to have
• Looking for either white, navy blue, or gray cards

```html
<!DOCTYPE html>
<html lang="en">
<head>
<meta charset="utf-8">
<title>Harlow Pemberton Insurance &amp; Investments – Stationery</title>
<link rel="stylesheet" href="https://fonts.googleapis.com/css2?family=Cinzel:wght@500&family=Open+Sans:wght@400;600&display=swap">
<style>
  :root {
    --navy: #2b3358;
    --navy-soft: #3a4266;
    --slate: #5d6a74;
    --slate-light: #7d8a93;
    --paper: #f7f7f5;
    --white: #ffffff;
    --ink: #3b3f4a;
    --icon: #8a8f98;
    --backdrop: #e9e7e3;
    --brand-font: "Cinzel", serif;
    --text-font: "Open Sans", sans-serif;
  }
  * { box-sizing: border-box; margin: 0; padding: 0; }
  html, body { width: 1200px; height: 984px; overflow: hidden; }
  body { background: var(--backdrop); font-family: var(--text-font); color: var(--ink); position: relative; }

  .brand { font-family: var(--brand-font); font-weight: 500; color: var(--navy); line-height: 1.1; text-align: center; white-space: nowrap; }
  .brand__name { display: block; letter-spacing: 0.03em; }
  .brand__line { display: block; letter-spacing: 0.03em; }
  .brand__mark { display: inline-block; border: 2px solid currentColor; }

  /* Letterhead */
  .letterhead {
    position: absolute; left: 40px; top: 60px; width: 608px; height: 860px;
    background: var(--paper); box-shadow: 0 2px 10px rgba(0,0,0,.15);
  }
  .letterhead__band { position: absolute; left: 0; top: 0; bottom: 0; width: 24px; background: var(--navy); }
  .letterhead__rule { position: absolute; left: 28px; top: 0; bottom: 0; width: 2px; background: var(--navy-soft); }
  .letterhead__contact { position: absolute; left: 70px; top: 52px; font-size: 10px; line-height: 15px; white-space: nowrap; }
  .contact-row { display: flex; align-items: center; gap: 6px; }
  .contact-row svg { width: 10px; height: 10px; flex: none; }
  .letterhead__address { margin-top: 10px; font-size: 10px; }
  .letterhead .brand { position: absolute; right: 40px; top: 44px; }
  .letterhead .brand__mark { width: 40px; height: 40px; margin-bottom: 6px; }
  .letterhead .brand__name { font-size: 20px; }
  .letterhead .brand__line { font-size: 9.5px; }

  /* Cards */
  .card { position: absolute; left: 720px; width: 440px; height: 251px; box-shadow: 0 2px 8px rgba(0,0,0,.18); overflow: hidden; }

  .card--slate { top: 60px; background: linear-gradient(160deg, var(--slate-light), var(--slate)); }
  .card--slate .brand { color: #d9dee2; position: absolute; left: 0; right: 0; top: 78px; }
  .card--slate .brand__name { font-size: 28px; }
  .card-tagline { position: absolute; left: 0; right: 0; bottom: 22px; text-align: center; font-size: 11px; letter-spacing: .06em; color: #e4e8eb; }

  .card--split { top: 367px; background: var(--white); display: flex; }
  .card--split .card__front { width: 62%; display: flex; align-items: center; justify-content: center; }
  .card--split .brand__mark { width: 30px; height: 30px; margin-bottom: 6px; }
  .card--split .brand__name { font-size: 18px; }
  .card--split .brand__line { font-size: 8.5px; }
  .card__back { width: 38%; background: var(--navy); color: var(--white); padding: 20px 14px; border-left: 4px double #c9ccd6; position: relative; }
  .person__name { font-size: 15px; font-family: var(--brand-font); font-weight: 500; }
  .person__role { font-size: 10px; margin-top: 2px; }
  .card__back .contact-list { margin-top: 70px; font-size: 8.5px; line-height: 13px; }
  .card__back .contact-row svg { width: 9px; height: 9px; }
  .card__back .contact-row svg circle { fill: #c9ccd6; }
  .card__back .address { margin-top: 14px; font-size: 8.5px; line-height: 12px; }

  .card--navy { top: 674px; background: var(--navy-soft); }
  .card--navy .brand { color: #b8bfcf; position: absolute; left: 0; right: 0; top: 58px; }
  .card--navy .brand__mark { width: 36px; height: 36px; margin-bottom: 8px; }
  .card--navy .brand__name { font-size: 21px; }
  .card--navy .brand__line { font-size: 9.5px; }
  .card--navy .card-tagline { color: #aab1c3; font-size: 9px; }
</style>
</head>
<body>

<section class="letterhead" aria-label="Letterhead">
  <div class="letterhead__band"></div>
  <div class="letterhead__rule"></div>
  <div class="letterhead__contact">
    <div class="contact-row"><svg viewBox="0 0 12 12"><circle cx="6" cy="6" r="6" fill="var(--icon)"/></svg>014.552.7310</div>
    <div class="contact-row"><svg viewBox="0 0 12 12"><circle cx="6" cy="6" r="6" fill="var(--icon)"/></svg>info@harlowpemberton.com</div>
    <div class="contact-row"><svg viewBox="0 0 12 12"><circle cx="6" cy="6" r="6" fill="var(--icon)"/></svg>www.hpbrokerage.com</div>
    <p class="letterhead__address">Suite 210, HP building, Ashford, Westland</p>
  </div>
  <div class="brand">
    <span class="brand__mark"></span>
    <span class="brand__name">Harlow Pemberton</span>
    <span class="brand__line">Insurance &amp; Investments</span>
  </div>
</section>

<section class="card card--slate" aria-label="Business card, slate front">
  <div class="brand"><span class="brand__name">Harlow Pemberton</span></div>
  <p class="card-tagline">Health, Life, Home, Auto, etc</p>
</section>

<section class="card card--split" aria-label="Business card, white and navy">
  <div class="card__front">
    <div class="brand">
      <span class="brand__mark"></span>
      <span class="brand__name">Harlow Pemberton</span>
      <span class="brand__line">Insurance &amp; Investments</span>
    </div>
  </div>
  <div class="card__back">
    <p class="person__name">YOUR NAME</p>
    <p class="person__role">Director</p>
    <div class="contact-list">
      <div class="contact-row"><svg viewBox="0 0 12 12"><circle cx="6" cy="6" r="5"/></svg>014.552.7310</div>
      <div class="contact-row"><svg viewBox="0 0 12 12"><circle cx="6" cy="6" r="5"/></svg>info@harlowpemberton.com</div>
      <div class="contact-row"><svg viewBox="0 0 12 12"><circle cx="6" cy="6" r="5"/></svg>www.hpbrokerage.com</div>
    </div>
    <p class="address">Suite 210, HP building,<br>Ashford, Westland</p>
  </div>
</section>

<section class="card card--navy" aria-label="Business card, navy front">
  <div class="brand">
    <span class="brand__mark"></span>
    <span class="brand__name">Harlow Pemberton</span>
    <span class="brand__line">Insurance &amp; Investments</span>
  </div>
  <p class="card-tagline">Health, Life, Home, Auto, etc</p>
</section>

</body>
</html>
```